WEB HOSTING COMPANY WHMCS THEME

The name of the web host company is "crane ember" so i would like something professional and simple. Il let you guys chouse the colors use your imagination on this, i will need a logo and a business card design. I would also like the theme coded and installed to my whims server and last thing we need to setup the website to go live at te end i will pay extra for that. Thank you

Target Market(s)

Web Hosting Company

Contact Information for Business Card

CRANEEMBER

Logo Text

CRANEEMBER

Coding

Coded - Design and coding required

Number of Pages Required

5+ page

Font styles to use
Sans Serif

Requirements
Must have
• EMAIL PHONE NUMBER MOBILE NUMBER WEBSITE AND BUSINESS ADRESS

```html
<!DOCTYPE html>
<html lang="en">
<head>
<meta charset="utf-8">
<title>Crane Ember — Web Hosting Automation</title>
<link href="https://fonts.googleapis.com/css2?family=Oswald:wght@400;500&family=Open+Sans:wght@400;600;700&display=swap" rel="stylesheet">
<style>
:root{
  --green:#5c9f0c;
  --green-dark:#4a860a;
  --ink:#222428;
  --text:#444;
  --muted:#666;
  --panel:#eeeeee;
  --tab:#eaeaea;
  --footer:#2a2a2a;
  --footer-bar:#1e1e1e;
  --white:#fff;
}
*{box-sizing:border-box;margin:0;padding:0}
html,body{width:1200px;height:3600px;overflow:hidden;background:var(--white)}
body{font-family:'Open Sans',Arial,sans-serif;color:var(--text);position:relative}
.page{position:relative;width:1200px;height:3600px;overflow:hidden}
.abs{position:absolute}
.heading{font-family:'Oswald',Arial,sans-serif;font-weight:500;color:var(--green);text-transform:uppercase;text-align:center;font-size:34px}
.rule{width:120px;height:3px;background:var(--green);margin:16px auto 0}
.para{font-size:15px;line-height:26px;text-align:center;color:var(--text)}

/* hero */
.hero{left:0;top:0;width:1200px;height:600px;background:linear-gradient(180deg,#1f2b1c 0%,#2f4a1e 45%,#3e6a1a 100%)}
.hero-curve{left:0;top:470px}
.brand{left:96px;top:28px;color:var(--white);font-family:'Open Sans',Arial,sans-serif;font-weight:600;font-size:36px;letter-spacing:-0.5px;display:flex;align-items:center;gap:10px}
.brand-mark{width:22px;height:22px;border:3px solid var(--white);border-radius:50%}
.nav{left:396px;top:40px;display:flex;gap:26px;align-items:center;font-size:15px;color:var(--white);text-transform:uppercase}
.nav .pill{border:2px solid var(--white);border-radius:24px;padding:7px 20px;font-weight:600}
.hero-title{left:0;top:196px;width:1200px;text-align:center;font-family:'Oswald',Arial,sans-serif;font-weight:500;font-size:54px;color:var(--white);letter-spacing:1px}
.hero-sub{left:0;top:290px;width:1200px;text-align:center;font-size:21px;font-weight:600;color:var(--white)}
.hero-input{left:418px;top:360px;width:200px;height:50px;background:var(--white);border-radius:25px;padding:0 22px;line-height:50px;font-size:16px;color:var(--muted)}
.hero-btn{left:632px;top:360px;width:150px;height:50px;background:var(--green);border:2px solid var(--white);border-radius:25px;line-height:46px;text-align:center;font-size:15px;font-weight:600;color:var(--white)}
.arrow-l{left:34px;top:282px}.arrow-r{left:1140px;top:282px}

/* welcome */
.welcome{left:98px;top:528px;width:1004px;height:594px;background:var(--white);border-top:5px solid var(--green);border-bottom:5px solid var(--green);box-shadow:0 2px 14px rgba(0,0,0,.15)}
.features{position:absolute;left:0;top:240px;width:100%;display:flex;justify-content:space-around;padding:0 40px}
.feature{width:260px;text-align:center}
.feature-icon{width:164px;height:164px;border-radius:50%;border:4px solid var(--ink);margin:0 auto;display:flex;align-items:center;justify-content:center}
.feature-icon.active{background:var(--green);border:none;box-shadow:0 0 0 8px #fff inset,0 0 0 12px var(--green) inset}
.feature h3{font-size:20px;font-weight:700;color:var(--ink);margin-top:38px}
.feature.active h3{color:var(--green);font-weight:600}
.feature p{font-size:14px;line-height:22px;margin-top:14px}

/* pricing */
.tabs{left:98px;top:1313px;width:1004px;height:70px;display:flex;background:var(--tab)}
.tab{flex:1;text-align:center;line-height:70px;font-family:'Oswald',Arial,sans-serif;font-size:26px;color:var(--ink);text-transform:uppercase}
.tab.active{background:var(--green);color:var(--white);position:relative}
.tab.active::after{content:"";position:absolute;left:50%;bottom:-22px;margin-left:-22px;border-left:22px solid transparent;border-right:22px solid transparent;border-top:22px solid var(--green)}
.plan{background:var(--panel);text-align:center;width:222px;height:302px;top:1481px}
.plan h4{font-family:'Oswald',Arial,sans-serif;font-weight:400;font-size:26px;color:var(--ink);margin-top:22px}
.plan .from{font-size:16px;color:var(--muted);margin-top:10px}
.plan .price{font-family:'Oswald',Arial,sans-serif;font-weight:500;font-size:40px;color:var(--green);margin-top:8px}
.plan p{font-size:13px;line-height:20px;margin:12px 30px 0}
.order{display:inline-block;margin-top:16px;border:2px solid #555;border-radius:22px;padding:7px 24px;font-size:13px;font-weight:600;color:var(--ink);text-transform:uppercase}
.plan.featured{left:437px;top:1450px;width:326px;height:364px;background:var(--green);color:var(--white);box-shadow:0 4px 16px rgba(0,0,0,.3)}
.plan.featured h4,.plan.featured .from,.plan.featured .price,.plan.featured p{color:var(--white)}
.plan.featured .order{border-color:var(--white);color:var(--white)}
.badge{display:inline-block;margin-top:26px;background:var(--white);color:var(--green);font-family:'Oswald',Arial,sans-serif;font-size:24px;padding:4px 28px}
.plan.featured h4{margin-top:8px}

/* services */
.servers{left:98px;top:2105px;width:413px;height:391px;background:linear-gradient(90deg,#0d0d0d,#2a2d33 50%,#0d0d0d)}
.service{left:600px;width:500px}
.service h5{font-family:'Oswald',Arial,sans-serif;font-weight:400;font-size:24px;color:var(--ink);text-transform:uppercase}
.service p{font-size:15px;line-height:25px;margin-top:10px}

/* news */
.news{left:0;top:2556px;width:1200px;height:631px;background:var(--panel)}
.news-card{top:2705px;width:317px;text-align:center}
.news-photo{width:317px;height:228px;position:relative}
.date{position:absolute;left:0;bottom:0;width:60px;text-align:center;color:var(--white);font-family:'Oswald',Arial,sans-serif;font-size:18px}
.date .m{background:#222;padding:8px 0 4px}
.date .d{background:var(--green);padding:4px 0 6px}
.date.plain .d{background:#222}
.news-card h6{font-size:19px;font-weight:600;color:var(--ink);margin-top:36px}
.news-card p{font-size:13px;line-height:21px;margin:12px 10px 0}
.more{display:inline-block;margin-top:20px;border:2px solid #555;border-radius:22px;padding:7px 26px;font-size:14px;font-weight:600;color:var(--ink)}
.more.solid{background:var(--green);border-color:var(--green);color:var(--white)}

/* footer */
.footer{left:0;top:3187px;width:1200px;height:351px;background:var(--footer);color:#ddd}
.footer h6{font-family:'Oswald',Arial,sans-serif;font-weight:400;font-size:24px;color:var(--white);text-transform:uppercase}
.footer .line{width:80px;height:2px;background:var(--green);margin-top:12px}
.footer p{font-size:13px;line-height:21px;margin-top:18px;color:#ddd}
.footer .link-more{font-family:'Oswald',Arial,sans-serif;color:var(--green);font-size:20px;margin-top:16px;display:block}
.footer ul{list-style:none;margin-top:14px}
.footer li{font-size:15px;padding:10px 0 10px 20px;border-bottom:1px solid #555;position:relative}
.footer li::before{content:"›";position:absolute;left:2px;top:7px;font-size:18px}
.bottom-bar{left:0;top:3538px;width:1200px;height:62px;background:var(--footer-bar);color:#ccc;font-size:13px;text-align:center;line-height:62px}
</style>
</head>
<body>
<div class="page">

  <!-- Hero -->
  <div class="abs hero" role="img" aria-label="Dark green tinted photo of a data centre aisle lined with server racks"></div>
  <svg class="abs hero-curve" width="1200" height="140" viewBox="0 0 1200 140"><path d="M0 60 Q600 -20 1200 60 L1200 140 L0 140 Z" fill="#fff"/></svg>
  <div class="abs brand"><span>craneember</span><span class="brand-mark"></span></div>
  <nav class="abs nav">
    <span>Features</span><span>Addons</span><span>Services</span><span>Partners</span><span>Marketplace</span><span>Login</span><span>More</span><span class="pill">Pricing</span>
  </nav>
  <svg class="abs arrow-l" width="26" height="52" viewBox="0 0 26 52"><path d="M24 2 L2 26 L24 50" stroke="#fff" stroke-width="2" fill="none"/></svg>
  <svg class="abs arrow-r" width="26" height="52" viewBox="0 0 26 52"><path d="M2 2 L24 26 L2 50" stroke="#fff" stroke-width="2" fill="none"/></svg>
  <h1 class="abs hero-title">WEB HOSTING AUTOMATION MADE EASY</h1>
  <p class="abs hero-sub">Nemo enim ipsam voluptatem quia voluptas &nbsp;aspernate</p>
  <div class="abs hero-input">Feature Tour</div>
  <div class="abs hero-btn">GET STARTED &gt;</div>

  <!-- Welcome -->
  <section class="abs welcome">
    <h2 class="heading" style="margin-top:46px">Welcome to Crane Ember</h2>
    <div class="rule"></div>
    <p class="para" style="margin:22px 60px 0">Lorem ipsum dolor sit amet, consectetur adipisicing elit. Rem atque, praesentium doloremque quae debitis odit quos quas atque commodi ipsa. Neque laborum animi illo amet provident, asperiores.</p>
    <div class="features">
      <div class="feature">
        <div class="feature-icon">
          <svg width="64" height="64" viewBox="0 0 64 64" fill="#222428"><rect x="22" y="4" width="20" height="16"/><rect x="31" y="20" width="2" height="12"/><rect x="8" y="31" width="48" height="2"/><rect x="8" y="31" width="2" height="12"/><rect x="31" y="31" width="2" height="12"/><rect x="54" y="31" width="2" height="12"/><rect x="1" y="43" width="16" height="14"/><rect x="24" y="43" width="16" height="14"/><rect x="47" y="43" width="16" height="14"/></svg>
        </div>
        <h3>Support</h3>
        <p>Lorem ipsum dolor sit amet, consectetur adipisicing elit. Rem atque, praesentium do loremque quae debitis.</p>
      </div>
      <div class="feature active">
        <div class="feature-icon active">
          <svg width="60" height="64" viewBox="0 0 60 64" fill="none" stroke="#fff" stroke-width="3"><path d="M10 10 H40 L50 20 V58 H10 Z"/><path d="M18 34 H42 M18 42 H42 M18 50 H34"/><path d="M36 8 c-6 0 -6 8 0 8 c6 0 6 8 0 8 M36 4 V28" stroke-width="2.5"/></svg>
        </div>
        <h3>Recurring Billing</h3>
        <p>Lorem ipsum dolor sit amet, consectetur adipisicing elit. Rem atque, praesentium do loremque quae debitis.</p>
      </div>
      <div class="feature">
        <div class="feature-icon">
          <svg width="64" height="64" viewBox="0 0 64 64"><rect x="30" y="2" width="4" height="10" fill="#222428"/><circle cx="32" cy="4" r="4" fill="#222428"/><rect x="10" y="12" width="44" height="30" rx="10" fill="#222428"/><rect x="4" y="22" width="6" height="12" fill="#222428"/><rect x="54" y="22" width="6" height="12" fill="#222428"/><rect x="16" y="20" width="32" height="14" rx="4" fill="#fff"/><circle cx="25" cy="27" r="3" fill="#222428"/><circle cx="39" cy="27" r="3" fill="#222428"/><path d="M14 44 H50 L46 62 H18 Z" fill="#222428"/></svg>
        </div>
        <h3>Automation</h3>
        <p>Lorem ipsum dolor sit amet, consectetur adipisicing elit. Rem atque, praesentium do loremque quae debitis.</p>
      </div>
    </div>
  </section>

  <!-- Pricing -->
  <div class="abs" style="left:0;top:1190px;width:1200px">
    <h2 class="heading">Popular Pricing</h2>
    <div class="rule"></div>
  </div>
  <div class="abs tabs">
    <div class="tab">Shared Hosting</div>
    <div class="tab active">VPS Hosting</div>
    <div class="tab">Dedicated Hosting</div>
  </div>
  <div class="abs plan" style="left:216px">
    <h4>Plan 1</h4><div class="from">Starting At</div><div class="price">$6.99</div>
    <p>Lorem ipsum dolor sit consectetur elit.</p><span class="order">Order Now</span>
  </div>
  <div class="abs plan" style="left:763px">
    <h4>Plan 3</h4><div class="from">Starting At</div><div class="price">$6.99</div>
    <p>Lorem ipsum dolor sit consectetur elit.</p><span class="order">Order Now</span>
  </div>
  <div class="abs plan featured">
    <span class="badge">POPULAR</span>
    <h4>Plan 3</h4><div class="from">Starting At</div><div class="price">$6.99</div>
    <p>Lorem ipsum dolor sit consectetur elit.</p><span class="order">Order Now</span>
  </div>

  <!-- Services -->
  <div class="abs" style="left:0;top:1898px;width:1200px">
    <h2 class="heading">Services Included</h2>
    <div class="rule"></div>
    <p class="para" style="margin:22px 150px 0">Lorem ipsum dolor sit amet, consectetur adipisicing elit. Rem atque, praesentium doloremque quae debitis odit quos quas atque commodi ipsa. Neque laborum animi illo amet provident, asperiores.</p>
  </div>
  <div class="abs servers" role="img" aria-label="Three black server rack cabinets with illuminated drive bays"></div>
  <svg class="abs" style="left:400px;top:2140px" width="200" height="280" viewBox="0 0 200 280">
    <g stroke="#5c9f0c" stroke-width="2"><line x1="22" y1="18" x2="180" y2="18"/><line x1="22" y1="137" x2="180" y2="137"/><line x1="22" y1="255" x2="180" y2="255"/></g>
    <g fill="#5c9f0c"><circle cx="22" cy="18" r="7"/><circle cx="22" cy="137" r="7"/><circle cx="22" cy="255" r="7"/></g>
  </svg>
  <div class="abs service" style="top:2142px"><h5>24/7/365 Support</h5><p>Lorem ipsum dolor sit amet, consectetur adipisicing elit. Non qui delectus ipsum iusto sit, hic voluptas, dicta deleniti.</p></div>
  <div class="abs service" style="top:2261px"><h5>45 Day Guarantee</h5><p>Lorem ipsum dolor sit amet, consectetur adipisicing elit. Non qui delectus ipsum iusto sit, hic voluptas, dicta deleniti.</p></div>
  <div class="abs service" style="top:2379px"><h5>99.9% Uptime</h5><p>Lorem ipsum dolor sit amet, consectetur adipisicing elit. Non qui delectus ipsum iusto sit, hic voluptas, dicta deleniti.</p></div>

  <!-- News -->
  <section class="abs news">
    <h2 class="heading" style="margin-top:52px">Latest News</h2>
    <div class="rule"></div>
  </section>
  <article class="abs news-card" style="left:98px">
    <div class="news-photo" role="img" aria-label="Blue-lit data centre with tall server cabinets" style="background:linear-gradient(135deg,#9fb6cc,#4f6a86)">
      <div class="date"><div class="m">AUG</div><div class="d">11</div></div>
    </div>
    <h6>Nemo enim ipsam voluptatem</h6>
    <p>Sed ut perspiciatis unde omnis iste natus error sit voluptatem accusantium doloremque laudantium, totam rem aperiam, eaque ipsum.</p>
    <span class="more solid">Read More</span>
  </article>
  <article class="abs news-card" style="left:442px">
    <div class="news-photo" role="img" aria-label="Technician working at an open server rack" style="background:linear-gradient(135deg,#5e6e7c,#2c3742)">
      <div class="date plain"><div class="m">AUG</div><div class="d">20</div></div>
    </div>
    <h6>Perspiciatis unde omnis</h6>
    <p>Sed ut perspiciatis unde omnis iste natus error sit voluptatem accusantium doloremque laudantium, totam rem aperiam, eaque ipsum.</p>
    <span class="more">Read More</span>
  </article>
  <article class="abs news-card" style="left:785px">
    <div class="news-photo" role="img" aria-label="Laptop keyboard with colourful app cubes floating above it" style="background:linear-gradient(135deg,#3a4f7a,#8a5aa8 60%,#d0905a)">
      <div class="date plain"><div class="m">AUG</div><div class="d">20</div></div>
    </div>
    <h6>Totam rem aperiam</h6>
    <p>Sed ut perspiciatis unde omnis iste natus error sit voluptatem accusantium doloremque laudantium, totam rem aperiam, eaque ipsum.</p>
    <span class="more">Read More</span>
  </article>

  <!-- Footer -->
  <footer class="abs footer">
    <div class="abs" style="left:98px;top:38px;width:500px">
      <h6>About Us</h6><div class="line"></div>
      <p>Lorem ipsum dolor sit amet, consectetur adipisicing elit. Laborum quod molli tia quisquam. Architecto quam in atque sint voluptatem, consequatur con sectetur illum doloremque laudantium ipsam maxime quod consequuntur excepturi illum dolorem ex modi.Lorem ipsum dolor sit amet, consectetur adipisicing elit. Consectetur animi id ex perspiciatis dis tinctio sequi minima...</p>
      <span class="link-more">Read More &gt;</span>
    </div>
    <div class="abs" style="left:668px;top:38px;width:214px">
      <h6>Services</h6><div class="line"></div>
      <ul><li>Shared Hosting</li><li>Reseller Hosting</li><li>VPS Hosting</li><li>Dedicated Hosting</li></ul>
    </div>
    <div class="abs" style="left:929px;top:38px;width:173px">
      <h6>Useful Links</h6><div class="line"></div>
      <ul><li>Features</li><li>Addons</li><li>Services</li><li>Partners</li><li>Marketplace</li></ul>
    </div>
  </footer>
  <div class="abs bottom-bar">Copyright © 2017 Crane Ember. All Rights Reserved.</div>

</div>
</body>
</html>
```